Design a Stylish Front Page For Our Skincare Brand Website

We have developed a luxurious and stylish skincare serum, and we need to get a stylish front page designed.
You will get a detailed website mockup to follow, and a detailed description of each part of the website.
This will give you a full understanding of what the goal, the style and requirements is.
For a detailed task description please go to:
https://pages.quorvantpad.net/sheet/d/7Qm2r-9TfaLwEkZ0pN4vHs8yXcB1jUe6dR__oGiVh3tq/view?mode=sharing
For your convenience the mockup is attached here, and the rest of the content you can find at the link above.
In case of any questions please always feel free to reach out to me here, or ask me for other communication platforms if you prefer.
We are looking forward to see your winning design!
Female 35 plus
Skincare
1 page

```html
<!DOCTYPE html>
<html lang="en">
<head>
<meta charset="utf-8">
<title>Lysvangen — Your Daily Beauty Insurance</title>
<link href="https://fonts.googleapis.com/css2?family=Cinzel:wght@400;600;700&family=Lato:wght@400;700&display=swap" rel="stylesheet">
<style>
:root{
  --teal:#19b3c5;
  --teal-dark:#2b6c7a;
  --ink:#1b1b1b;
  --body:#6f6f6f;
  --gold-a:#6b5535;
  --gold-b:#d9c6a0;
  --white:#ffffff;
  --black:#000000;
  --photo-grey:#c9c6c2;
}
*{box-sizing:border-box;margin:0;padding:0}
html,body{width:1200px;height:4082px;overflow:hidden;background:var(--white)}
body{position:relative;font-family:'Lato',sans-serif;color:var(--ink)}
.abs{position:absolute}
.serif{font-family:'Cinzel',serif}
.btn{position:absolute;display:flex;align-items:center;justify-content:center;border-radius:30px;
  background:linear-gradient(90deg,var(--gold-a),var(--gold-b) 55%,var(--gold-a));
  color:var(--white);font-family:'Cinzel',serif;font-weight:700;font-size:14px;letter-spacing:.5px;
  box-shadow:0 4px 10px rgba(0,0,0,.2)}
.photo{position:absolute;border-radius:14px}
.frame{position:absolute;border:4px solid var(--teal);border-radius:12px}
.h2{position:absolute;font-family:'Cinzel',serif;font-weight:700;font-size:34px;line-height:45px;color:var(--ink)}
.para{position:absolute;font-size:14.5px;line-height:25.7px;color:var(--body);text-align:justify}

/* header */
.topbar{left:404px;top:0;width:796px;height:44px;background:var(--teal);clip-path:polygon(40px 0,100% 0,100% 100%,0 100%)}
.topbar-item{position:absolute;top:10px;color:var(--white);font-size:15px;display:flex;align-items:center;gap:8px}
.login{position:absolute;left:986px;top:6px;width:103px;height:30px;border:2px solid var(--white);border-radius:16px;
  color:var(--white);font-family:'Cinzel',serif;font-weight:700;font-size:13px;display:flex;align-items:center;justify-content:center;gap:8px}
.logo{font-family:'Cinzel',serif;font-weight:400;color:var(--ink);letter-spacing:5px}
.nav a{position:absolute;top:67px;font-size:15px;color:var(--ink);text-decoration:none}
.nav .active{color:var(--teal)}
.header-line{left:0;top:104px;width:1200px;height:2px;background:#e6e6e6}

/* footer */
.foot-h{position:absolute;font-family:'Cinzel',serif;font-weight:700;font-size:19px;color:var(--white)}
.foot-t{position:absolute;font-size:14.5px;line-height:24px;color:var(--white)}
</style>
</head>
<body>

<!-- Header -->
<header>
  <div class="abs topbar"></div>
  <div class="topbar-item" style="left:484px">
    <svg width="12" height="16" viewBox="0 0 12 16"><path d="M6 0a6 6 0 0 0-6 6c0 4.5 6 10 6 10s6-5.5 6-10a6 6 0 0 0-6-6zm0 8.5A2.5 2.5 0 1 1 6 3.5a2.5 2.5 0 0 1 0 5z" fill="#fff"/></svg>
    Lorem ipsum dolor sit amet, consectetur
  </div>
  <div class="topbar-item" style="left:810px">
    <svg width="14" height="14" viewBox="0 0 24 24"><path d="M6.6 10.8a15 15 0 0 0 6.6 6.6l2.2-2.2a1 1 0 0 1 1-.25 11.4 11.4 0 0 0 3.6.57 1 1 0 0 1 1 1V20a1 1 0 0 1-1 1A17 17 0 0 1 3 4a1 1 0 0 1 1-1h3.5a1 1 0 0 1 1 1c0 1.25.2 2.45.57 3.6a1 1 0 0 1-.25 1z" fill="#fff"/></svg>
    +1 555 010 2040
  </div>
  <div class="login">
    <svg width="12" height="12" viewBox="0 0 24 24"><circle cx="12" cy="7" r="5" fill="#fff"/><path d="M2 23c0-6 4.5-9 10-9s10 3 10 9z" fill="#fff"/></svg>
    LOGIN
  </div>
  <div class="abs logo" style="left:111px;top:34px;font-size:34px">LYSVANGEN</div>
  <nav class="nav">
    <a class="active" style="left:490px">Home</a>
    <a style="left:571px">About Us</a>
    <a style="left:674px">Contact</a>
    <a style="left:769px">Order Tracking</a>
    <a style="left:935px">
      <svg width="14" height="13" viewBox="0 0 24 22" style="vertical-align:-1px;margin-right:8px"><path d="M0 1h4l3 12h13l3-9H7" fill="none" stroke="#19b3c5" stroke-width="3"/><circle cx="9" cy="19" r="2.5" fill="#19b3c5"/><circle cx="19" cy="19" r="2.5" fill="#19b3c5"/></svg>Cart</a>
    <a style="left:1011px">
      <svg width="14" height="14" viewBox="0 0 24 24" style="vertical-align:-2px;margin-right:8px"><circle cx="10" cy="10" r="7" fill="none" stroke="#19b3c5" stroke-width="3.5"/><path d="M15 15l7 7" stroke="#19b3c5" stroke-width="3.5"/></svg>Search</a>
  </nav>
  <div class="abs" style="left:490px;top:101px;width:38px;height:4px;background:var(--teal)"></div>
  <div class="abs header-line"></div>
</header>

<!-- Hero -->
<section class="hero">
  <div class="abs" role="img" aria-label="Woman in a towel touching her face in a bright bathroom" style="left:0;top:106px;width:1200px;height:700px;background:linear-gradient(90deg,#6f6a66 0%,#a29a94 35%,#c9c5c1 65%,#8f8d8c 100%)"></div>
  <div class="abs" style="left:0;top:106px;width:1200px;height:700px;background:linear-gradient(90deg,rgba(0,0,0,.35),rgba(0,0,0,0) 60%)"></div>
  <div class="abs" style="left:741px;top:302px;width:378px;height:378px;border-radius:50%;background:rgba(120,205,210,.6)"></div>
  <div class="abs" role="img" aria-label="Teal serum bottle with gold dropper cap" style="left:830px;top:248px;width:180px;height:422px;border-radius:20px 20px 14px 14px;background:linear-gradient(180deg,#f2f2f2 0%,#d7c39a 12%,#a88b5a 24%,#1f8d9a 30%,#2aa9b8 60%,#17737f 100%)"></div>
  <h1 class="abs serif" style="left:111px;top:330px;font-size:42px;font-weight:700;color:var(--white);letter-spacing:.5px">Your Daily Beauty Insurance</h1>
  <p class="abs" style="left:111px;top:388px;width:600px;font-size:15px;line-height:26px;color:var(--white)">Lorem ipsum dolor sit amet, consectetur adipiscing elit, sed do eiusmod tempor incididunt ut labore et dolore magna aliqua.</p>
  <div class="btn" style="left:111px;top:460px;width:147px;height:52px">Shop Now</div>
  <svg class="abs" style="left:0;top:600px" width="1200" height="215" viewBox="0 0 1200 215">
    <path d="M0,215 L0,194 C230,110 420,95 640,150 C860,205 1040,160 1200,92 L1200,215 Z" fill="#fff"/>
    <path d="M80,188 C260,96 430,80 640,135 C840,185 960,195 1088,170 C950,215 800,212 630,170 C430,120 270,128 80,188 Z" fill="#19b3c5"/>
  </svg>
</section>

<!-- Feature 1 -->
<section>
  <div class="frame" style="left:111px;top:872px;width:370px;height:416px"></div>
  <div class="photo" role="img" aria-label="Woman in a cosy sweater looking at her phone in bed" style="left:163px;top:921px;width:370px;height:418px;background:linear-gradient(160deg,#2c4a6e,#7a8ea3 55%,#c4c9cf)"></div>
  <h2 class="h2" style="left:583px;top:920px;width:540px">Protect Your Face From Daily Free Radicals</h2>
  <p class="para" style="left:583px;top:1020px;width:486px">Daily and harmful free radicals help to break down your face's support system, which is scientifically proven to be the basis for wrinkles. When your face's support system is also what is called collagen, and when your collagen level is broken down for several hours every single day with smartphone, computer, TV, etc., then in 2022 it is more important than ever that you protect your face from free radicals such as also called blueight.</p>
  <div class="btn" style="left:583px;top:1224px;width:147px;height:52px">Learn More</div>
</section>

<!-- Feature 2 -->
<section>
  <div class="frame" style="left:666px;top:1422px;width:369px;height:417px"></div>
  <div class="photo" role="img" aria-label="Mature woman smiling with close-up circles showing skin detail" style="left:716px;top:1469px;width:371px;height:419px;background:linear-gradient(160deg,#e6e6e6,#cfcfcf 60%,#d8c3b2)"></div>
  <h2 class="h2" style="left:130px;top:1483px;width:500px">Block Wrinkles Before They Occur</h2>
  <p class="para" style="left:130px;top:1586px;width:482px">With your daily protection from LYSVANGEN, your serum goes in and gives your face a very special nourishment that produces more daily collagen. Collagen is your face support system and with LYSVANGEN serum you block the breakdown of collagen which is the same as "blocking" wrinkles by making your skin as strong as possible BEFORE the wrinkles see the light of day.</p>
  <div class="btn" style="left:130px;top:1762px;width:147px;height:54px">Learn More</div>
</section>

<!-- Feature 3 -->
<section>
  <div class="frame" style="left:111px;top:1997px;width:370px;height:416px"></div>
  <div class="photo" role="img" aria-label="Woman with closed eyes resting her hands on her cheek" style="left:163px;top:2045px;width:370px;height:420px;background:linear-gradient(160deg,#e8e6e4,#c9aa95 55%,#e0d8d2)"></div>
  <h2 class="h2" style="left:583px;top:2045px;width:520px">Boost Your Daily Cell Renewal</h2>
  <p class="para" style="left:583px;top:2146px;width:486px">With our completely unique and newly manufactured (patent pending) form, you get exactly the daily protection your skin needs to keep wrinkles and bags away. Throughout the day, you will be protected with our carefully crafted form, which makes sure to give your face exactly the extracts and ingredients needed for your cell renewal to take place at an optimal and stable pace, which gives you the best cell renewal, to maintain a youthful look.</p>
  <div class="btn" style="left:583px;top:2349px;width:147px;height:52px">Learn More</div>
</section>

<!-- Security guarantee -->
<section>
  <div class="abs" role="img" aria-label="Laboratory worker in gloves testing products" style="left:0;top:2545px;width:1200px;height:362px;background:linear-gradient(120deg,#3a7c8b,#2a6877 50%,#1f5a68)"></div>
  <h2 class="abs serif" style="left:0;top:2607px;width:1200px;text-align:center;font-size:34px;font-weight:700;color:var(--white)">Your Security Guarantee</h2>
  <p class="abs" style="left:195px;top:2670px;width:810px;text-align:center;font-size:14.5px;line-height:25.7px;color:var(--white)">All products are legally and thoroughly tested in a technologically advanced laboratory that ensures that all products live 100% up to market standards, and all legal and safety requirements are met so you can always feel safe when using products from LYSVANGEN.</p>
  <div class="btn" style="left:526px;top:2773px;width:148px;height:50px">Order Now</div>
</section>

<!-- Brand showcase -->
<section>
  <h2 class="abs serif" style="left:111px;top:2984px;width:480px;font-size:35px;line-height:46px;font-weight:700">Lysvangen - Protect You Most Beautiful Property</h2>
  <p class="para" style="left:766px;top:2982px;width:322px;color:#9a9a9a">With the careful selection of high quality ingredients and a patent pending formula, you get the necessary and daily beauty insurance that protects and nurtures your beauty throughout the day.</p>
  <div class="btn" style="left:766px;top:3124px;width:145px;height:54px">Learn More</div>
  <div class="photo" role="img" aria-label="Cream jars and bottles with green leaves" style="left:13px;top:3194px;width:210px;height:280px;border-radius:8px;background:linear-gradient(160deg,#e9d9cf,#d7bfb3)"></div>
  <div class="photo" role="img" aria-label="Skincare oils and creams with herbs" style="left:235px;top:3194px;width:210px;height:280px;border-radius:8px;background:linear-gradient(160deg,#e7e2d2,#c8bd98)"></div>
  <div class="abs" style="left:460px;top:3099px;width:280px;height:380px;background:var(--white);box-shadow:0 4px 18px rgba(0,0,0,.12)"></div>
  <div class="abs" role="img" aria-label="Teal serum bottle with gold dropper cap" style="left:540px;top:3140px;width:110px;height:300px;border-radius:14px;background:linear-gradient(180deg,#eee 0%,#c9b38a 20%,#1f8d9a 32%,#2aa9b8 70%,#9fdbe2 100%)"></div>
  <div class="photo" role="img" aria-label="Amber dropper bottles beside coral" style="left:756px;top:3194px;width:209px;height:280px;border-radius:8px;background:linear-gradient(160deg,#e8cbb4,#c79a78)"></div>
  <div class="photo" role="img" aria-label="Green pump bottle and cotton pads on blue wood" style="left:976px;top:3194px;width:211px;height:280px;border-radius:8px;background:linear-gradient(160deg,#a9cfe0,#7fb6cf)"></div>
</section>

<!-- Footer -->
<footer>
  <svg class="abs" style="left:0;top:3560px" width="1200" height="160" viewBox="0 0 1200 160">
    <path d="M0,160 L0,108 C200,60 400,70 620,110 C860,150 1040,110 1200,22 L1200,160 Z" fill="#000"/>
    <path d="M112,48 C300,10 460,20 640,55 C830,92 980,82 1118,30 C990,118 820,128 630,95 C440,62 290,50 112,48 Z" fill="#19b3c5"/>
  </svg>
  <div class="abs" style="left:0;top:3715px;width:1200px;height:367px;background:var(--black)"></div>
  <div class="abs logo" style="left:111px;top:3742px;font-size:34px;color:var(--white)">LYSVANGEN</div>
  <svg class="abs" style="left:118px;top:3804px" width="10" height="14" viewBox="0 0 12 16"><path d="M6 0a6 6 0 0 0-6 6c0 4.5 6 10 6 10s6-5.5 6-10a6 6 0 0 0-6-6zm0 8.5A2.5 2.5 0 1 1 6 3.5a2.5 2.5 0 0 1 0 5z" fill="#fff"/></svg>
  <div class="foot-t" style="left:143px;top:3798px">Lorem ipsum dolor sit<br>amet, consectetur</div>
  <svg class="abs" style="left:116px;top:3864px" width="15" height="11" viewBox="0 0 15 11"><rect width="15" height="11" rx="1" fill="#fff"/><path d="M0 1l7.5 5L15 1" fill="none" stroke="#000" stroke-width="1.3"/></svg>
  <div class="foot-t" style="left:143px;top:3857px">info@lysvangen.com</div>
  <svg class="abs" style="left:117px;top:3897px" width="13" height="13" viewBox="0 0 24 24"><path d="M6.6 10.8a15 15 0 0 0 6.6 6.6l2.2-2.2a1 1 0 0 1 1-.25 11.4 11.4 0 0 0 3.6.57 1 1 0 0 1 1 1V20a1 1 0 0 1-1 1A17 17 0 0 1 3 4a1 1 0 0 1 1-1h3.5a1 1 0 0 1 1 1c0 1.25.2 2.45.57 3.6a1 1 0 0 1-.25 1z" fill="#fff"/></svg>
  <div class="foot-t" style="left:143px;top:3892px">+1 555 010 2040</div>

  <div class="foot-h" style="left:434px;top:3740px">Quick Link</div>
  <div class="foot-t" style="left:437px;top:3786px;line-height:30px">Home<br>About Us<br>Contact<br>&nbsp;Order Tracking</div>

  <div class="foot-h" style="left:615px;top:3740px">Help Link</div>
  <div class="foot-t" style="left:617px;top:3786px;line-height:30px">Terms&amp;condtions<br>Privacy Policy<br>About Us<br>Support</div>

  <div class="foot-h" style="left:793px;top:3740px;font-size:18px">Subscribe To Our Newsletter</div>
  <div class="foot-t" style="left:795px;top:3786px;width:300px">Lorem ipsum dolor sit amet, consectetur adipiscing elit, sed do</div>
  <div class="abs" style="left:794px;top:3853px;width:273px;height:40px;border-radius:20px;background:var(--white)"></div>
  <div class="abs" style="left:814px;top:3864px;font-size:14.5px;color:#9a9a9a">Enter Your Email</div>
  <div class="abs" style="left:1028px;top:3858px;width:32px;height:30px;border-radius:50%;background:var(--teal);display:flex;align-items:center;justify-content:center">
    <svg width="14" height="14" viewBox="0 0 24 24"><path d="M2 11L22 2l-7 20-4-8z" fill="#fff"/></svg>
  </div>
  <div class="abs" style="left:803px;top:3922px;width:30px;height:30px;border-radius:50%;background:var(--white)"></div>
  <div class="abs" style="left:842px;top:3922px;width:30px;height:30px;border-radius:50%;background:var(--white)"></div>
  <div class="abs" style="left:881px;top:3922px;width:30px;height:30px;border-radius:50%;background:var(--white)"></div>
  <div class="abs" style="left:921px;top:3922px;width:30px;height:30px;border-radius:50%;background:var(--white)"></div>

  <div class="abs" style="left:95px;top:3990px;width:1010px;height:1px;background:#2a2a2a"></div>
  <div class="abs" style="left:0;top:4022px;width:1200px;text-align:center;font-size:14.5px;color:var(--white)">©Copyrights 2022&nbsp; Lysvangen&nbsp;&nbsp; |&nbsp;&nbsp;&nbsp; All Rights Reserved</div>
</footer>

</body>
</html>
```